Coverneugestaltung einer Zeitschrift für Betroffene mit Allergien
Zielgruppe
Wir sind ein medizinischer Verlag und geben Patientenzeitschriften heraus. Das Magazin 'Pollenara' richtet sich an Betroffene mit Allergien, Nahrungsmittelunverträglichkeiten, Lungen- und Hauterkrankungen
Aufgabenstellung
Das Cover sollte modern und seriös wirken. Die rote Ecke unten rechts "Ihr Exemplar zum Mitnehmen" muss zwingend unten rechts übernommen werden. Die Covergestaltung sollte so sein, dass zukünftig verschiedene Titelbilder verwendet werden können (u.a. Freisteller). Die Zeitschrift "Pollenara" erscheint viermal im Jahr.
Es darf alles verändert werden, Schrift, Farbe, Wort-Bild-Marke etc. Wir sind hier offen für Neues.

```html
<!DOCTYPE html>
<html lang="de">
<head>
<meta charset="utf-8">
<title>Pollenara – Cover</title>
<link href="https://fonts.googleapis.com/css2?family=Varela+Round&family=Open+Sans:wght@400;600;700&display=swap" rel="stylesheet">
<style>
  :root {
    --stage: #e4e4e2;
    --paper: #ffffff;
    --purple: #4a2560;
    --green: #8dbb3c;
    --red: #c4061c;
    --sky-top: #cfe6ec;
    --sky-mid: #f3f9fb;
    --haze: #a9cbd6;
    --forest: #4f7a4a;
    --rock: #c08a5a;
    --rock-dark: #8d5a3a;
  }
  html, body {
    margin: 0;
    width: 1200px;
    height: 913px;
    overflow: hidden;
    background: var(--stage);
  }
  .cover {
    position: absolute;
    left: 291px;
    top: 20px;
    width: 617px;
    height: 873px;
    background: var(--paper);
    box-shadow: 0 6px 18px rgba(0,0,0,.18);
  }
  .cover__frame {
    position: absolute;
    inset: 16px;
    border-radius: 0 28px 0 28px;
    overflow: hidden;
  }
  .cover__photo {
    position: absolute;
    inset: 0;
    background:
      linear-gradient(180deg,
        var(--sky-top) 0%,
        var(--sky-mid) 30%,
        #e6f1f4 45%,
        var(--haze) 52%,
        var(--forest) 64%,
        #6b7a48 70%,
        var(--rock) 76%,
        #d29a62 86%,
        var(--rock-dark) 100%);
  }
  .masthead {
    position: absolute;
    left: 30px;
    top: 62px;
    font-family: "Varela Round", sans-serif;
    font-size: 118px;
    line-height: 1;
    color: var(--purple);
    letter-spacing: -3px;
    white-space: nowrap;
  }
  .issue {
    position: absolute;
    right: 58px;
    top: 52px;
    font-family: "Open Sans", sans-serif;
    font-weight: 700;
    font-size: 12px;
    color: var(--purple);
    white-space: nowrap;
  }
  .tagline {
    position: absolute;
    right: 0;
    top: 196px;
    width: 236px;
    height: 34px;
    background: var(--green);
    color: #fff;
    font-family: "Open Sans", sans-serif;
    font-weight: 600;
    font-size: 13px;
    letter-spacing: 1.2px;
    line-height: 34px;
    padding-left: 22px;
    box-sizing: border-box;
    white-space: nowrap;
  }
  .topics {
    position: absolute;
    left: 0;
    top: 548px;
    margin: 0;
    padding: 0;
    list-style: none;
  }
  .topic {
    height: 40px;
    margin-bottom: 12px;
    background: var(--purple);
    border-radius: 0 12px 12px 0;
    color: #fff;
    font-family: "Open Sans", sans-serif;
    font-size: 14.5px;
    letter-spacing: 1.6px;
    line-height: 40px;
    padding-left: 48px;
    box-sizing: border-box;
    white-space: nowrap;
  }
  .topic--travel { width: 330px; }
  .topic--rehab { width: 450px; }
  .topic--skin { width: 390px; }
  .takeaway {
    position: absolute;
    right: 0;
    bottom: 0;
    width: 176px;
    height: 176px;
  }
  .takeaway__text {
    position: absolute;
    right: 14px;
    bottom: 40px;
    width: 110px;
    transform: rotate(-50deg);
    transform-origin: center;
    color: #fff;
    font-family: "Open Sans", sans-serif;
    font-size: 11px;
    line-height: 1.25;
    text-align: center;
  }
</style>
</head>
<body>
  <div class="cover">
    <div class="cover__frame">
      <div class="cover__photo" role="img" aria-label="Titelbild: Person mit ausgebreiteten Armen auf einem Felsplateau vor weiter, bewaldeter Berglandschaft im Morgendunst"></div>
      <div class="issue">Ausgabe 00/2018</div>
      <div class="masthead">pollenara</div>
      <div class="tagline">ALLERGIE | HAUT | LUNGE</div>
      <ul class="topics">
        <li class="topic topic--travel">REISEN MIT ALLERGIEN</li>
        <li class="topic topic--rehab">REHABILITATION BEI ASTHMA &amp; COPD</li>
        <li class="topic topic--skin">BEHANDLUNG VON ROSAZEA</li>
      </ul>
      <svg class="takeaway" viewBox="0 0 176 176" aria-hidden="true">
        <polygon points="176,0 176,176 0,176" fill="var(--red)"/>
      </svg>
      <div class="takeaway__text">Ihr Exemplar<br>zum<br>Mitnehmen</div>
    </div>
  </div>
</body>
</html>
```